Zielgruppe
Wir sind ein kleiner familiengeführter Weinbaubetrieb am Wagram und suchen einen modernen und naturnahen Namen und ein Etikett mit Blickfang für unseren Wermut, aus handgepflückten regionalen Wildkräutern mit Rosewein vom Zweigelt. Charakeristik des Getränks: Aperitif, Zitrusnote, leichte Bitternote, mit Tonic water als Cocktail.
Unsere Zielgruppe: kaufkräftige Genussmenschen im mittleren Alter
Aufgabenstellung
Etikett für 0,5l Flasche, Flasche noch nicht festgelegt, Etikettenhöhe: 65mm
Was soll draufstehen: Name, Vermouth, local botanicals, handcrafted, small batch

```html
<!DOCTYPE html>
<html lang="en">
<head>
<meta charset="utf-8">
<title>Vermouth Rose – Label</title>
<link rel="stylesheet" href="https://fonts.googleapis.com/css2?family=Poiret+One&family=Cormorant+Garamond:wght@400&family=Ubuntu:wght@400&display=swap">
<style>
  :root {
    --page: #ffffff;
    --frame: #2f6a93;
    --frame-light: #4f87ad;
    --orange: #cf6426;
    --orange-light: #e79a68;
    --vermouth-red: #e2465a;
    --rose-blue: #6f8fb8;
    --text-blue: #3a5aa8;
    --soft-blue: #7ea2c9;
    --navy: #2c2a86;
    --badge: #2a5f8c;
    --hatch: #e8733a;
  }
  * { margin: 0; padding: 0; box-sizing: border-box; }
  html, body {
    width: 1200px; height: 1200px; overflow: hidden;
    background: var(--page);
  }
  .canvas { position: relative; width: 1200px; height: 1200px; }

  .label {
    position: absolute;
    left: 307px; top: 81px;
    width: 667px; height: 1180px;
    transform: scale(0.88);
    transform-origin: top left;
    background: linear-gradient(90deg, var(--frame-light), var(--frame) 20%, var(--frame) 80%, var(--frame-light));
    padding: 14px;
  }
  .label-panel {
    position: relative;
    width: 100%; height: 100%;
    background: linear-gradient(90deg, var(--orange-light) 0%, var(--orange) 22%, var(--orange) 70%, var(--orange-light) 100%);
    overflow: hidden;
  }

  .product-name {
    position: absolute;
    left: 56px; top: 60px;
    writing-mode: vertical-rl;
    font-family: "Poiret One", sans-serif;
    font-size: 112px;
    line-height: 1;
    letter-spacing: 14px;
    color: var(--vermouth-red);
  }

  .brand-badge {
    position: absolute;
    left: 368px; top: 46px;
    width: 216px; height: 216px;
    border-radius: 50%;
    background: var(--badge);
    display: flex; align-items: center; justify-content: center;
  }
  .brand-name {
    font-family: "Ubuntu", sans-serif;
    font-size: 28px;
    color: var(--soft-blue);
    text-align: center;
    line-height: 1.15;
  }

  .hatch-accent {
    position: absolute;
    left: 390px; top: 470px;
    width: 250px; height: 330px;
    background: linear-gradient(135deg, transparent 35%, rgba(232,115,58,0.55) 60%, rgba(240,140,90,0.35) 85%, transparent);
    clip-path: polygon(100% 0, 100% 60%, 20% 100%, 0 100%);
  }

  .variety {
    position: absolute;
    left: 62px; top: 790px;
    font-family: "Cormorant Garamond", serif;
    font-size: 52px;
    letter-spacing: 4px;
    color: var(--rose-blue);
  }
  .rule {
    position: absolute;
    left: 62px; width: 512px; height: 2px;
    background: var(--soft-blue);
  }
  .rule-top { top: 850px; }
  .rule-bottom { top: 924px; }

  .claims {
    position: absolute;
    left: 62px; top: 862px;
    font-family: "Ubuntu", sans-serif;
    font-size: 39px;
    color: var(--text-blue);
    white-space: nowrap;
  }
  .batch {
    position: absolute;
    left: 73px; top: 934px;
    font-family: "Ubuntu", sans-serif;
    font-size: 27px;
    color: var(--soft-blue);
  }
  .grape-mark {
    position: absolute;
    left: 85px; top: 985px;
    width: 115px; height: 145px;
    border-radius: 45% 45% 50% 50% / 35% 35% 65% 65%;
    background: radial-gradient(circle at 50% 35%, rgba(110,110,200,0.45), rgba(110,110,200,0.2));
  }
  .divider {
    position: absolute;
    left: 255px; top: 932px;
    width: 2px; height: 170px;
    background: var(--soft-blue);
  }
  .specs {
    position: absolute;
    left: 297px; top: 935px;
    font-family: "Ubuntu", sans-serif;
    color: var(--navy);
    letter-spacing: 8px;
  }
  .abv { font-size: 58px; line-height: 1.3; }
  .abv small { font-size: 32px; letter-spacing: 4px; }
  .volume { font-size: 62px; line-height: 1.3; }
</style>
</head>
<body>
<main class="canvas">
  <section class="label">
    <div class="label-panel">
      <h1 class="product-name">VERMOUTH</h1>

      <div class="brand-badge">
        <span class="brand-name">Hollwart<br>Reben</span>
      </div>

      <div class="hatch-accent" role="img" aria-label="Diagonal line hatching accent"></div>

      <p class="variety">ROSE</p>
      <div class="rule rule-top"></div>
      <p class="claims">local botanicals | handcrafted</p>
      <div class="rule rule-bottom"></div>

      <p class="batch">small batch</p>
      <div class="grape-mark" role="img" aria-label="Grape cluster illustration"></div>
      <div class="divider"></div>

      <div class="specs">
        <p class="abv">17%<small>vol</small></p>
        <p class="volume">500ml</p>
      </div>
    </div>
  </section>
</main>
</body>
</html>
```